ultra-minimalist business card

front (black background, matte):

samir t. kouri
writer | photographer
get@samirkouri.com

back (white background, matte):

a picture speaks a thousand words;
a word draws a thousand pictures.

www.samirkouri.com

all text should be small (white or silver - as long as it shows against the black - on the front; black or gray - as long as it shows against the white - on the back).

feel free to get creative in terms of arrangement, alignment, and font type, but remember, the overall style is minimalist, so nothing too fancy, please.

thanks.

```html
<!DOCTYPE html>
<html lang="en">
<head>
<meta charset="utf-8">
<title>Samir T. Kouri — Business Card</title>
<link rel="stylesheet" href="https://fonts.googleapis.com/css2?family=Questrial&display=swap">
<style>
  :root {
    --canvas-bg: #ececec;
    --card-light-top: #f7f7f7;
    --card-light-bottom: #e4e4e4;
    --card-dark-top: #2e2e2e;
    --card-dark-bottom: #262626;
    --ink-dark: #1c1c1c;
    --ink-light: #f2f2f2;
    --ink-silver: #d6d6d6;
    --rule-dark: #1c1c1c;
    --rule-light: #e6e6e6;
  }

  * { box-sizing: border-box; margin: 0; padding: 0; }

  html, body {
    width: 1200px;
    height: 586px;
    overflow: hidden;
    background: var(--canvas-bg);
    font-family: "Questrial", "Century Gothic", sans-serif;
  }

  .canvas {
    position: relative;
    width: 1200px;
    height: 586px;
  }

  .card {
    position: absolute;
    top: 129px;
    width: 501px;
    height: 301px;
    overflow: hidden;
  }

  .card--back  { left: 62px; }
  .card--front { left: 619px; }

  .card__texture {
    position: absolute;
    inset: 0;
    width: 100%;
    height: 100%;
  }

  .card--back .card__texture {
    background: linear-gradient(160deg, var(--card-light-top), var(--card-light-bottom));
  }

  .card--front .card__texture {
    background: linear-gradient(160deg, var(--card-dark-top), var(--card-dark-bottom));
  }

  .card__text {
    position: absolute;
    left: 0;
    right: 0;
    text-align: center;
    white-space: nowrap;
  }

  /* Back: quote */
  .motto {
    top: 115px;
    color: var(--ink-dark);
    font-size: 15px;
    line-height: 27px;
  }

  /* Front: identity */
  .identity__name {
    top: 114px;
    color: var(--ink-light);
    font-size: 19px;
    letter-spacing: 0.5px;
  }

  .identity__role {
    top: 144px;
    color: var(--ink-silver);
    font-size: 12.5px;
    letter-spacing: 3.2px;
  }

  .card__rule {
    position: absolute;
    top: 262px;
    height: 1px;
  }

  .card--back .card__rule {
    left: 33px;
    width: 442px;
    background: var(--rule-dark);
  }

  .card--front .card__rule {
    left: 26px;
    width: 449px;
    background: var(--rule-light);
  }

  .card__contact {
    top: 268px;
    font-size: 13px;
  }

  .card--back .card__contact {
    color: var(--ink-dark);
    letter-spacing: 2.4px;
  }

  .card--front .card__contact {
    color: var(--ink-light);
    letter-spacing: 0.4px;
  }
</style>
</head>
<body>
  <main class="canvas">

    <section class="card card--back" aria-label="Card back">
      <div class="card__texture" role="img" aria-label="Soft white low-poly faceted geometric texture"></div>
      <p class="card__text motto">
        A Picture Speaks A Thousand Words<br>
        A Word Draws A Thousand Pictures
      </p>
      <div class="card__rule"></div>
      <p class="card__text card__contact">www.samirkouri.com</p>
    </section>

    <section class="card card--front" aria-label="Card front">
      <div class="card__texture" role="img" aria-label="Dark charcoal low-poly faceted geometric texture"></div>
      <h1 class="card__text identity__name">Samir T. Kouri</h1>
      <p class="card__text identity__role">Writer&nbsp;&nbsp;|&nbsp;&nbsp;Photographer</p>
      <div class="card__rule"></div>
      <p class="card__text card__contact">get@samirkouri.com</p>
    </section>

  </main>
</body>
</html>
```